Dr. Lumora needs a design for its website!

*Only need the design, coding is not required.
*Need desktop version ($500) and mobile/tablet version ($200)
*The attached files are not the exact layout we want, they are just for you to know what information should be included in those pages.
*The function of our website is like www.qtv-medlist.example
*For the background picture, prefer a lively picture and chinese people in it, NOT necessarily need a doctor or sick person in the picture

***Don't just copy the layout from the attachments or from the reference website, we are looking for creative ideas, non-ordinary designs!!!****

We are developing a website for the public to search a doctor by different criteria. At the initial stage, we need 4 pages to start with and other pages at later stage. I have attached the general idea of these pages but not necessarily to be exactly the same, I am looking for some new ideas.

This website needs a professional, modern, simple and user friendly design. The main color to be used in the website will be same as the color (R:0 G:139 B:205) used in our logo (see attached). We don't have any particular thoughts for the other color and the font to be used in the website. Can try to use circle outline for the icon in the navigation bar.

1. Home: will include 4 sections (see attached)

2. Doctor's details (see attached)

3. Health information: will include a short descriptions of this Health Info page and 5 sections (see attached)

4. News (see attached)

Reason: Not too many suitable designs to choose from and need more time to go through the designs

Target Market(s)

All

Industry/Entity Type

Medical

Number of Pages Required

4 page

Requirements
Should not have
• must not be same as or looks too much like www.qtv-medlist.example
• prefer not to use black and red color

```html
<!DOCTYPE html>
<html lang="en">
<head>
<meta charset="utf-8">
<title>Dr. Lumora – Find a Doctor</title>
<link rel="stylesheet" href="https://fonts.googleapis.com/css2?family=Oxygen:wght@400;700&family=Open+Sans:wght@400;600&display=swap">
<style>
  :root {
    --brand: #0a88cd;
    --brand-dark: #0878b8;
    --accent: #d32a2a;
    --ink: #2b2b2b;
    --muted: #555;
    --line: #c9c9c9;
    --panel: rgba(255,255,255,0.9);
    --row-tint: #deedf6;
    --white: #fff;
  }
  * { box-sizing: border-box; margin: 0; padding: 0; }
  html, body { width: 1193px; height: 1200px; overflow: hidden; background: var(--white); }
  body { font-family: "Oxygen", sans-serif; color: var(--ink); }
  .page { position: relative; width: 1193px; height: 1200px; overflow: hidden; }

  /* Header */
  .site-header { position: absolute; left: 0; top: 0; width: 100%; height: 135px; }
  .brand { position: absolute; left: 78px; top: 34px; display: flex; align-items: center; gap: 12px; }
  .brand-dot { width: 58px; height: 58px; border-radius: 50%; background: var(--brand); }
  .brand-name { font-family: "Open Sans", sans-serif; font-weight: 600; font-size: 36px; color: var(--brand); letter-spacing: -0.5px; }
  .lang { position: absolute; top: 59px; left: 884px; display: flex; align-items: center; gap: 28px; font-family: "Open Sans", sans-serif; font-size: 12px; color: #111; }
  .lang-select { width: 130px; height: 24px; border: 1px solid var(--line); display: flex; align-items: center; padding: 0 7px; gap: 8px; font-size: 15px; color: #777; position: relative; }
  .lang-swatch { width: 20px; height: 13px; background: #1f3f8a; }
  .lang-caret { position: absolute; right: 10px; top: 10px; border: 4px solid transparent; border-top: 5px solid #222; }

  /* Navigation */
  .main-nav { position: absolute; top: 135px; left: 0; width: 100%; height: 49px; background: var(--brand); }
  .nav-item { position: absolute; top: 0; height: 49px; line-height: 49px; color: var(--white); font-size: 15.5px; letter-spacing: 0.3px; }
  .nav-item.is-active { background: var(--accent); width: 90px; text-align: center; }
  .nav-search { position: absolute; left: 865px; top: 9px; width: 248px; height: 31px; background: var(--white); display: flex; align-items: center; padding: 0 10px; font-family: "Open Sans", sans-serif; font-size: 13px; color: #999; justify-content: space-between; }

  /* Hero background */
  .hero-bg { position: absolute; left: 0; top: 184px; width: 100%; height: 930px;
    background: linear-gradient(180deg, #9fb0b8 0%, #c4d2d6 30%, #d3e0e3 55%, #e6eef0 78%, #ffffff 100%); }

  .panel { position: absolute; background: var(--panel); }
  .field-label { position: absolute; font-size: 15px; letter-spacing: 0.3px; color: var(--ink); }
  .field { position: absolute; height: 37px; border: 1px solid var(--line); background: var(--white); }
  .field.select::after { content: ""; position: absolute; right: 11px; top: 16px; border: 5px solid transparent; border-top: 7px solid #333; }
  .btn { position: absolute; height: 35px; color: var(--white); font-size: 15px; display: flex; align-items: center; justify-content: center; gap: 12px; letter-spacing: 0.3px; }
  .btn.red { background: var(--accent); }
  .btn.blue { background: var(--brand); }

  .radio { position: absolute; display: flex; align-items: center; gap: 12px; font-size: 15px; }
  .radio-dot { width: 21px; height: 21px; border: 1px solid #888; border-radius: 50%; position: relative; }
  .radio-dot.is-on::after { content: ""; position: absolute; left: 6px; top: 6px; width: 7px; height: 7px; border-radius: 50%; background: #222; }

  .search-panel { left: 77px; top: 231px; width: 484px; height: 384px; }
  .login-panel { left: 620px; top: 231px; width: 483px; height: 232px; }
  .member-panel { left: 620px; top: 498px; width: 483px; height: 250px; }
  .panel-title { position: absolute; left: 27px; font-size: 22px; letter-spacing: 0.5px; color: var(--ink); }
  .forgot { position: absolute; left: 226px; top: 192px; font-family: "Open Sans", sans-serif; font-size: 13px; color: #555; text-decoration: underline; }
  .benefits { position: absolute; left: 30px; top: 76px; list-style: none; }
  .benefits li { height: 29.4px; display: flex; align-items: center; gap: 8px; font-family: "Open Sans", sans-serif; font-size: 15px; color: #555; letter-spacing: 0.2px; }

  /* Results table */
  .results { position: absolute; left: 77px; top: 800px; width: 1029px; height: 294px; border: 1px solid var(--brand); border-top: none; background: var(--white); font-family: "Open Sans", sans-serif; }
  .results-row { display: grid; grid-template-columns: 116px 128px 150px 123px 100px 132px 125px 1fr; padding-left: 36px; align-items: center; }
  .results-head { height: 45px; background: var(--brand); color: var(--white); font-size: 16px; }
  .results-body .results-row { height: 83px; font-size: 15.5px; color: #333; }
  .results-body .results-row:nth-child(odd) { background: var(--row-tint); }
  .results-body .results-row > span:nth-child(3) { padding-left: 5px; }
  .results-body .results-row > span:nth-child(8) { padding-left: 0; margin-left: -3px; }
  .gender-icon { width: 25px; height: 25px; border-radius: 50%; background: var(--brand); margin-left: 3px; }

  /* Footer */
  .site-footer { position: absolute; left: 0; top: 1135px; width: 100%; border-top: 1px solid #ccc; text-align: center; padding-top: 24px; font-family: "Open Sans", sans-serif; font-size: 15.5px; color: #666; }
</style>
</head>
<body>
<div class="page">
  <header class="site-header">
    <div class="brand">
      <span class="brand-dot"></span>
      <span class="brand-name">Dr. Lumora</span>
    </div>
    <div class="lang">
      <span>Select Language</span>
      <div class="lang-select"><span class="lang-swatch"></span>English<span class="lang-caret"></span></div>
    </div>
  </header>

  <nav class="main-nav">
    <a class="nav-item is-active" style="left:72px">HOME</a>
    <a class="nav-item" style="left:197px">TBC</a>
    <a class="nav-item" style="left:283px">HEALTH INFO</a>
    <a class="nav-item" style="left:436px">NEWS</a>
    <a class="nav-item" style="left:535px">ABOUT US</a>
    <a class="nav-item" style="left:666px">CONTACT US</a>
    <div class="nav-search">
      <span>Search</span>
      <svg width="22" height="22" viewBox="0 0 22 22"><circle cx="9" cy="9" r="7" fill="none" stroke="#111" stroke-width="2.6"/><line x1="14" y1="14" x2="20" y2="20" stroke="#111" stroke-width="3" stroke-linecap="round"/></svg>
    </div>
  </nav>

  <div class="hero-bg" role="img" aria-label="Softly blurred photo of medical staff walking down a bright hospital corridor"></div>

  <section class="panel search-panel">
    <span class="field-label" style="left:27px;top:43px">DOCTOR'S NAME:</span>
    <div class="field" style="left:189px;top:29px;width:257px"></div>

    <span class="field-label" style="left:27px;top:91px">GENDER:</span>
    <label class="radio" style="left:156px;top:86px"><span class="radio-dot is-on"></span>MALE</label>
    <label class="radio" style="left:260px;top:86px"><span class="radio-dot"></span>FEMALE</label>

    <span class="field-label" style="left:27px;top:139px">SPECIALISM:</span>
    <div class="field select" style="left:189px;top:128px;width:257px"></div>

    <span class="field-label" style="left:27px;top:187px">SYMPTONS:</span>
    <div class="field select" style="left:189px;top:175px;width:257px"></div>

    <span class="field-label" style="left:27px;top:235px">DISTRICT:</span>
    <div class="field select" style="left:189px;top:223px;width:257px"></div>

    <span class="field-label" style="left:27px;top:283px">PHONE NUMBER:</span>
    <div class="field" style="left:189px;top:270px;width:257px"></div>

    <a class="btn red" style="left:201px;top:327px;width:102px">RESET</a>
    <a class="btn blue" style="left:318px;top:327px;width:129px">SEARCH
      <svg width="20" height="20" viewBox="0 0 22 22"><circle cx="9" cy="9" r="7" fill="none" stroke="#fff" stroke-width="2.6"/><line x1="14" y1="14" x2="20" y2="20" stroke="#fff" stroke-width="3" stroke-linecap="round"/></svg>
    </a>
  </section>

  <section class="panel login-panel">
    <h2 class="panel-title" style="top:30px;font-weight:400">MEMBER LOGIN</h2>
    <span class="field-label" style="left:30px;top:85px">LOGIN EMAIL:</span>
    <div class="field" style="left:146px;top:76px;width:305px"></div>
    <span class="field-label" style="left:30px;top:137px">PASSWORD:</span>
    <div class="field" style="left:146px;top:127px;width:305px"></div>
    <a class="forgot">Forgot Password</a>
    <a class="btn red" style="left:348px;top:181px;width:102px">LOGIN</a>
  </section>

  <section class="panel member-panel">
    <h2 class="panel-title" style="left:30px;top:26px;font-weight:400">BECOME A DR. LUMORA MEMBER</h2>
    <ul class="benefits">
      <li><svg width="14" height="12" viewBox="0 0 14 12"><path d="M1 6l4 4 8-9" fill="none" stroke="#d32a2a" stroke-width="2"/></svg>First-hand health news</li>
      <li><svg width="14" height="12" viewBox="0 0 14 12"><path d="M1 6l4 4 8-9" fill="none" stroke="#d32a2a" stroke-width="2"/></svg>Exclusive Promotions</li>
      <li><svg width="14" height="12" viewBox="0 0 14 12"><path d="M1 6l4 4 8-9" fill="none" stroke="#d32a2a" stroke-width="2"/></svg>Instant Health Advices</li>
      <li><svg width="14" height="12" viewBox="0 0 14 12"><path d="M1 6l4 4 8-9" fill="none" stroke="#d32a2a" stroke-width="2"/></svg>Free Health seminars/talks</li>
      <li><svg width="14" height="12" viewBox="0 0 14 12"><path d="M1 6l4 4 8-9" fill="none" stroke="#d32a2a" stroke-width="2"/></svg>Priority doctor appointments</li>
    </ul>
  </section>

  <section class="results">
    <div class="results-row results-head">
      <span>Name</span><span>Gender</span><span>Specialism</span><span>Private</span><span>XXX</span><span>Address</span><span>District</span><span>Phone</span>
    </div>
    <div class="results-body">
      <div class="results-row"><span>XXX</span><span><span class="gender-icon" style="display:block"></span></span><span>XXX</span><span>Private</span><span>XXX</span><span>XXXXX</span><span>XXX</span><span>21234567</span></div>
      <div class="results-row"><span>XXX</span><span><span class="gender-icon" style="display:block"></span></span><span>XXX</span><span>Private</span><span>XXX</span><span>XXXXX</span><span>XXX</span><span>21234568</span></div>
      <div class="results-row"><span>XXX</span><span><span class="gender-icon" style="display:block"></span></span><span>XXX</span><span>Private</span><span>XXX</span><span>XXXXX</span><span>XXX</span><span>21234569</span></div>
    </div>
  </section>

  <footer class="site-footer">All contents copyright © Dr. Lumora 2016 All rights reserved.</footer>
</div>
</body>
</html>
```